Moon River Healing Buisness Cards

I am looking to create a business card for a healing business. In the business I provide coaching and Reiki. I am a licensed LCPC (licensed clinical professional counselor)

Moon River Healing
Soul Centered Healing, Reiki Healinig

Lena Vasquez, L.C.P.C

The card should include the following
biz name: Moon River Healing
my name: Lena Vasquez
website: Lenavasquez.example
email: lena.dorwin@mailbox.example
instagram handle: lenadorwinvasquez

Target Market(s)

Women ages 25-65

```html
<!DOCTYPE html>
<html lang="en">
<head>
<meta charset="utf-8">
<title>Moon River Healing – Business Cards</title>
<link rel="stylesheet" href="https://fonts.googleapis.com/css2?family=Cinzel:wght@500;700&family=Tinos&display=swap">
<style>
  :root {
    --backdrop: #d9d4cc;
    --card-black: #070707;
    --card-black-edge: #1c1c1c;
    --ink-white: #ffffff;
    --accent-blue: #3fb8e2;
    --ink-black: #0a0a0a;
    --galaxy-core: #ffffff;
    --galaxy-mid: #8fd0f5;
    --galaxy-outer: #2d7fd6;
    --galaxy-deep: #1e3fae;
    --divider: #5a5a5a;
  }
  * { margin: 0; padding: 0; box-sizing: border-box; }
  html, body {
    width: 900px; height: 1200px; overflow: hidden;
    background: var(--backdrop);
  }
  .canvas { position: relative; width: 900px; height: 1200px; }
  .card {
    position: absolute; left: 88px; width: 732px; height: 428px;
    border-radius: 22px; overflow: hidden;
  }
  .card-front {
    top: 126px;
    background: radial-gradient(ellipse at 50% 20%, var(--card-black-edge), var(--card-black) 70%);
  }
  .brand-mark {
    position: absolute; left: 150px; top: 124px; width: 200px; height: 180px;
    display: flex; flex-direction: column; align-items: center; justify-content: center;
    gap: 10px; font-family: "Cinzel", serif; font-weight: 500; text-align: center;
  }
  .brand-mark .mark-dot {
    width: 34px; height: 34px; border-radius: 50%; border: 3px solid currentColor;
  }
  .brand-mark .mark-name { font-size: 22px; line-height: 1.15; letter-spacing: 1px; }
  .card-front .brand-mark { color: var(--ink-white); }
  .divider {
    position: absolute; left: 364px; top: 118px; width: 1px; height: 192px;
    background: var(--divider);
  }
  .details { position: absolute; left: 401px; top: 118px; color: var(--ink-white); }
  .biz-name { font-family: "Cinzel", serif; font-weight: 700; line-height: 1; }
  .biz-name .line-main { display: block; font-size: 27px; letter-spacing: 0.5px; }
  .biz-name .line-sub {
    display: block; font-size: 21px; color: var(--accent-blue);
    letter-spacing: 4.6px; margin-top: 3px; font-weight: 500;
  }
  .person-name {
    font-family: "Cinzel", serif; font-weight: 700; font-size: 18px;
    margin-top: 24px; letter-spacing: 0.5px;
  }
  .contact-list { list-style: none; margin-top: 10px; font-family: "Tinos", serif; font-size: 16.5px; }
  .contact-list li { display: flex; align-items: center; gap: 12px; height: 27px; }
  .contact-icon { width: 19px; height: 19px; flex: none; }
  .card-back {
    top: 640px;
    background: radial-gradient(ellipse 60% 45% at 42% 42%, var(--galaxy-core) 0%, var(--galaxy-mid) 35%, var(--galaxy-outer) 70%, var(--galaxy-deep) 100%);
  }
  .card-back .brand-mark { left: 266px; top: 98px; color: var(--ink-black); }
  .back-title {
    position: absolute; left: 0; right: 0; top: 287px; text-align: center;
    font-family: "Cinzel", serif; font-weight: 700; font-size: 26px;
    color: var(--ink-black); letter-spacing: 0.3px;
  }
</style>
</head>
<body>
<main class="canvas">
  <section class="card card-front">
    <div class="brand-mark">
      <span class="mark-dot"></span>
      <span class="mark-name">Moon River<br>Healing</span>
    </div>
    <span class="divider"></span>
    <div class="details">
      <h1 class="biz-name"><span class="line-main">MOON RIVER</span><span class="line-sub">HEALING</span></h1>
      <p class="person-name">LENA VASQUEZ</p>
      <ul class="contact-list">
        <li>
          <svg class="contact-icon" viewBox="0 0 20 20" fill="none" stroke="var(--accent-blue)" stroke-width="1.5">
            <circle cx="10" cy="10" r="8"/><ellipse cx="10" cy="10" rx="3.5" ry="8"/><line x1="2" y1="10" x2="18" y2="10"/>
          </svg>
          <span>Lenavasquez.example</span>
        </li>
        <li>
          <svg class="contact-icon" viewBox="0 0 20 20">
            <rect x="1" y="4" width="18" height="12" fill="var(--accent-blue)"/>
            <polyline points="1,4 10,11 19,4" fill="none" stroke="var(--card-black)" stroke-width="1.4"/>
          </svg>
          <span>lena.dorwin@mailbox.example</span>
        </li>
        <li>
          <svg class="contact-icon" viewBox="0 0 20 20">
            <circle cx="10" cy="10" r="7.5" fill="none" stroke="var(--accent-blue)" stroke-width="1.6"/>
          </svg>
          <span>lenadorwinvasquez</span>
        </li>
      </ul>
    </div>
  </section>

  <section class="card card-back" role="img" aria-label="Bright blue spiral galaxy with glowing stars filling the card">
    <div class="brand-mark">
      <span class="mark-dot"></span>
      <span class="mark-name">Moon River<br>Healing</span>
    </div>
    <p class="back-title">MOON RIVER HEALING</p>
  </section>
</main>
</body>
</html>
```